Internet Service Tech provider product flyer redesign - Skyloft Netlink

We have created the attached flyer in Word and also attached a PDF. All the content is correct. We just need a complete re-design of the flyer with new relevant hi-res images (based on content) and a more streamlined/cleaner layout.

This product is an entire in-building WIFI system for Body's Corporate in High Rise buildings.

We are a Brisbane-based internet tech company that specialises in providing solutions for High Rise buildings

Body text style - Helvetica Light

Internet

```html
<!DOCTYPE html>
<html lang="en">
<head>
<meta charset="utf-8">
<title>Skyloft Netlink – flyer for body's corporate</title>
<link rel="stylesheet" href="https://fonts.googleapis.com/css2?family=Roboto:ital,wght@0,300;0,400;0,700;1,300&display=swap">
<style>
  :root {
    --red: #9b1b1b;
    --red-bright: #c41f1f;
    --red-dark: #6e0f0f;
    --grey-text: #3a3a3a;
    --grey-soft: #9a9a9a;
    --page: #f6f6f6;
    --stage: #ffffff;
    --sky-light: #eef2f6;
  }
  * { box-sizing: border-box; margin: 0; padding: 0; }
  html, body { width: 1200px; height: 822px; overflow: hidden; background: var(--stage); }
  body { font-family: "Roboto", Helvetica, Arial, sans-serif; font-weight: 300; color: var(--grey-text); position: relative; }

  .page { position: absolute; top: 50px; width: 510px; height: 723px; overflow: hidden; border: 1px solid #e2e2e2; }

  /* Cover */
  .cover { left: 77px; background: var(--sky-light); }
  .cover__photo { position: absolute; inset: 0;
    background: linear-gradient(160deg, #dfe6ee 0%, #f4f6f9 35%, #cfd8e2 60%, #f2f4f7 100%); }
  .cover__accent { position: absolute; left: 280px; top: 300px; width: 230px; height: 423px;
    background: linear-gradient(to right, rgba(180, 30, 30, 0) 0%, rgba(180, 30, 30, 0.55) 45%, #a8191b 100%); }
  .brand { position: absolute; left: 20px; top: 32px; display: flex; align-items: center; gap: 8px; }
  .brand__dot { width: 38px; height: 38px; border-radius: 50%; background: var(--red-bright); }
  .brand__name { font-weight: 700; color: var(--red-bright); font-size: 19px; line-height: 1; letter-spacing: 0.5px; }
  .cover__title { position: absolute; left: 16px; top: 513px; font-size: 40px; font-weight: 300; color: var(--red); letter-spacing: -0.5px; }
  .cover__subtitle { position: absolute; left: 18px; top: 563px; font-size: 22px; color: var(--grey-soft); }
  .cover__points { position: absolute; left: 16px; top: 664px; width: 320px; list-style: none; font-size: 7.6px; line-height: 16px; color: #8a8a8a; white-space: nowrap; }
  .cover__points b { color: var(--red); font-weight: 400; }

  /* Inside */
  .inside { left: 651px; background: var(--page); }
  .inside__heading { position: absolute; left: 38px; top: 54px; font-size: 26.5px; line-height: 32px; font-weight: 300; color: var(--red); }
  .inside__band { position: absolute; left: 0; top: 145px; width: 36px; height: 200px; background: var(--red); }
  .inside__photo { position: absolute; left: 36px; top: 145px; width: 261px; height: 200px;
    background: radial-gradient(circle at 35% 45%, #9aa0a6 0%, #5c6066 45%, #2c2e31 100%); }
  .inside__intro { position: absolute; left: 304px; top: 146px; width: 192px; font-size: 8.4px; line-height: 10.6px; text-align: justify; color: #333; }
  .quote { position: absolute; left: 306px; top: 288px; width: 190px; font-size: 11px; line-height: 15px; font-style: italic; color: var(--red); }
  .quote__mark { font-family: Georgia, serif; font-style: normal; font-weight: 700; font-size: 30px; line-height: 0; color: var(--red-dark); vertical-align: -10px; }
  .stat { position: absolute; left: 35px; top: 356px; font-size: 11px; color: var(--grey-soft); }
  .inside__offer { position: absolute; left: 35px; top: 403px; width: 440px; font-size: 8.4px; line-height: 11px; color: #333; }

  .benefits { position: absolute; left: 35px; top: 463px; display: flex; gap: 34px; }
  .benefit { width: 128px; }
  .benefit__tag { display: flex; align-items: center; height: 16px; margin-bottom: 6px; }
  .benefit__tag svg { width: 20px; height: 20px; margin-right: -2px; position: relative; z-index: 1; }
  .benefit__label { background: var(--red); color: #fff; font-size: 8px; padding: 2px 8px; white-space: nowrap; }
  .benefit__text { font-size: 8.6px; line-height: 11px; color: #333; }

  .contact { position: absolute; left: 33px; top: 664px; display: flex; font-size: 8.4px; line-height: 11.5px; color: var(--grey-soft); }
  .contact__title { display: block; font-size: 14px; color: var(--red); margin-bottom: 4px; line-height: 1; }
  .contact__col { padding-right: 12px; }
  .contact__col + .contact__col { border-left: 1.5px solid var(--red); padding-left: 12px; padding-top: 18px; height: 48px; margin-top: -2px; }
  .contact a { color: var(--grey-soft); text-decoration: underline; }
</style>
</head>
<body>

<section class="page cover">
  <div class="cover__photo" role="img" aria-label="Upward view of glass high-rise towers against a pale sky"></div>
  <div class="cover__accent" role="img" aria-label="Decorative red sweeping curves"></div>
  <div class="brand">
    <span class="brand__dot"></span>
    <span class="brand__name">TALLWAVE NETWORKS</span>
  </div>
  <h1 class="cover__title">Skyloft Netlink</h1>
  <p class="cover__subtitle">for body's corporate</p>
  <ul class="cover__points">
    <li><b>BULK SUPPLY</b> of fibre-grade Internet speeds delivered to all residents at wholesale prices</li>
    <li><b>HD WIFI</b> designed specifically for high rise buildings, using next-generation WIFI technology</li>
    <li><b>AUTOMATED BILLING</b> and payment system that's simple, easy to use and available 24/7</li>
  </ul>
</section>

<section class="page inside">
  <h2 class="inside__heading">Why Body's Corporate need to provide<br>Skyloft Netlink?</h2>
  <div class="inside__band"></div>
  <div class="inside__photo" role="img" aria-label="Businessman sketching a cloud network linking laptops, phones and servers"></div>
  <p class="inside__intro">The demand and consumption of digital content and the way it is delivered to tenants, owners, guests, and consumers is increasing exponentially every day. This massive increase in digital demand means Body's Corporate need to ensure that their buildings Communication, Internet and WIFI infrastructure is upgraded properly to cater for such mass amounts of digital demand by residents.</p>
  <p class="quote"><span class="quote__mark">“</span>Internet is now considered by many as a utility, just like water, gas and electricity<span class="quote__mark">”</span></p>
  <p class="stat">On average, every Australian has 2.6* wireless devices.</p>
  <p class="inside__offer">We can help Body's Corporate plan, project manage and bulk supply all aspects of upgrading and implementing a Skyloft Netlink build that is designed from the ground up for high-rise buildings.</p>

  <div class="benefits">
    <div class="benefit">
      <div class="benefit__tag">
        <svg viewBox="0 0 20 20" aria-hidden="true"><path d="M7 3h6M8 3v6L3 17h14l-5-8V3" fill="#222" stroke="#222" stroke-width="1.5"/><circle cx="12" cy="5" r="1.5" fill="#c41f1f"/></svg>
        <span class="benefit__label">meet resident demand</span>
      </div>
      <p class="benefit__text">Ensure that your building/s residents have access to proper digital connectivity, fibre-grade speed Internet, and HD WIFI using a bulk supply service that is scalable with future usage and growth</p>
    </div>
    <div class="benefit">
      <div class="benefit__tag">
        <svg viewBox="0 0 20 20" aria-hidden="true"><rect x="2" y="9" width="8" height="5" rx="2.5" transform="rotate(-45 6 11.5)" fill="none" stroke="#222" stroke-width="2.2"/><rect x="9" y="5" width="8" height="5" rx="2.5" transform="rotate(-45 13 7.5)" fill="none" stroke="#222" stroke-width="2.2"/></svg>
        <span class="benefit__label">increase building value</span>
      </div>
      <p class="benefit__text">Help owners/investors increase their ROI on their apartments by providing bulk high speed Internet services that's delivered through a state of the art HD WIFI system designed for your building</p>
    </div>
    <div class="benefit">
      <div class="benefit__tag">
        <svg viewBox="0 0 20 20" aria-hidden="true"><circle cx="10" cy="10" r="8" fill="none" stroke="#222" stroke-width="2"/><path d="M6 14l8-8M12 6h2v2" stroke="#222" stroke-width="2" fill="none"/></svg>
        <span class="benefit__label">fully managed service</span>
      </div>
      <p class="benefit__text">Our connected community platform is a complete managed service which helps minimize a Body's Corporate involvement in the day-to-day operations, and resident billing of the services</p>
    </div>
  </div>

  <footer class="contact">
    <div class="contact__col">
      <span class="contact__title">Get in touch</span>
      PO Box 5182<br>Brisbane QLD 4001
    </div>
    <div class="contact__col">Phone 1300 555 214<br>Fax 1300 555 219</div>
    <div class="contact__col"><a href="mailto:info@tallwavenet.com.au">info@tallwavenet.com.au</a><br><a href="#">www.tallwavenet.com.au</a></div>
  </footer>
</section>

</body>
</html>
```